Financial Advisor needs a BOLD Business Card

I need a business card that is professional, and is also eye-catching and memorable. I would like to include my photo (several different professional photos have been uploaded). Preferred primary color is blue, or green, or dark purple. The final design should have a modern/contemporary look while communicating a professional image.

Target Market(s)

Individual Investors and Small Business Owners

Industry/Entity Type

Business

Contact Information for Business Card

[side 1:] Dale Varkonen Financial Advisor 58217 Marlow Brook Rd., #240 St. Louis, MO 63975 (314) 555-0187 main (314) 555-0142 cell (314) 555-0169 fax dalev@qrmvbk.com [side 2:] Life Insurance | Retirement | Employee Benefits

Font styles to use
Serif
Sans Serif

Requirements
Must have
• [disclaimer, text can be 7-9 point:] Securities offered through the K.R. Capital Trading Company. Member BLUDA/TAVK. Nine Harbor Circle, Cincinnati, Ohio 45817. 513-555-0123. Investment Advisory Services offered through K.R. Portfolio Stewardship Company.
Nice to have
• Bright, Light & Airy feel on Side 1 with contact data, bold patterns, high color contrast, modern or 3D look
Should not have
• Any symbols referring to money (e.g. $)

```html
<!DOCTYPE html>
<html lang="en">
<head>
<meta charset="utf-8">
<title>Dale Varkonen – Financial Advisor Business Card</title>
<link rel="stylesheet" href="https://fonts.googleapis.com/css2?family=Roboto:wght@400;500;700&family=Montserrat:wght@500;600&display=swap">
<style>
  :root {
    --bg: #e9e7e3;
    --charcoal: #22272c;
    --charcoal-deep: #15191d;
    --charcoal-light: #2d3339;
    --blue: #2f86c8;
    --blue-bright: #4aa3e3;
    --blue-deep: #1d5f93;
    --white: #ffffff;
    --ink: #1c1f22;
    --grey-soft: #d9dde1;
    --grey-mid: #8c949b;
    --grey-fine: #9aa2a9;
    --text-light: #f2f4f6;
  }
  * { margin: 0; padding: 0; box-sizing: border-box; }
  html, body {
    width: 1200px; height: 784px; overflow: hidden;
    background: var(--bg);
    font-family: "Roboto", Arial, sans-serif;
  }
  .canvas {
    width: 1200px; height: 784px;
    display: flex; flex-direction: column;
    align-items: center; justify-content: center; gap: 24px;
  }
  .card {
    position: relative;
    width: 640px; height: 366px;
    overflow: hidden;
    box-shadow: 0 6px 18px rgba(0,0,0,0.22);
  }

  /* ---------- Back side ---------- */
  .card--back {
    background: radial-gradient(ellipse at 40% 30%, var(--charcoal-light), var(--charcoal) 55%, var(--charcoal-deep));
  }
  .services {
    position: absolute; left: 60px; top: 128px;
    transform: rotate(-8deg); transform-origin: left center;
    font-family: "Montserrat", Arial, sans-serif;
    font-weight: 500; font-size: 15px;
    font-variant: small-caps; letter-spacing: 2.5px;
    color: var(--blue-bright);
    white-space: nowrap;
  }
  .services .sep { color: var(--grey-mid); margin: 0 8px; }
  .back-brand {
    position: absolute; right: 48px; bottom: 110px;
    display: flex; align-items: center; gap: 10px;
  }
  .brand-square {
    width: 26px; height: 26px; background: var(--blue);
  }
  .back-brand .brand-text { display: flex; flex-direction: column; }
  .back-brand .brand-name {
    font-weight: 500; font-size: 20px; color: var(--blue-bright);
  }
  .back-brand .brand-role {
    font-family: "Montserrat", Arial, sans-serif;
    font-size: 8px; letter-spacing: 3px; text-transform: uppercase;
    color: var(--text-light); margin-top: 2px;
  }
  .disclaimer {
    position: absolute; left: 48px; right: 48px; bottom: 22px;
    font-size: 9px; line-height: 13px; text-align: center;
    color: var(--grey-fine);
  }

  /* ---------- Front side ---------- */
  .card--front { background: var(--charcoal); }
  .front-shapes { position: absolute; inset: 0; }
  .front-brand {
    position: absolute; left: 52px; top: 86px;
    display: flex; align-items: center;
  }
  .front-brand .brand-square { width: 54px; height: 54px; }
  .front-divider {
    width: 1px; height: 70px; background: var(--grey-mid);
    margin: 0 16px 0 22px;
  }
  .front-brand .brand-name {
    font-weight: 500; font-size: 31px; color: var(--blue);
    line-height: 1;
  }
  .front-brand .brand-role {
    font-family: "Montserrat", Arial, sans-serif;
    font-weight: 600; font-size: 11px; letter-spacing: 5px;
    text-transform: uppercase; color: var(--ink);
    margin-top: 8px;
  }
  .portrait {
    position: absolute; right: 54px; top: 16px;
    width: 138px; height: 172px;
    background: linear-gradient(180deg, #dfe3e7 0%, #9aa3ab 45%, #2c3137 100%);
  }
  .contact {
    position: absolute; left: 40px; top: 226px;
    list-style: none;
    color: var(--text-light); font-size: 15px; line-height: 19px;
  }
  .contact li { display: flex; align-items: flex-start; gap: 8px; }
  .contact svg { width: 14px; height: 14px; margin-top: 2px; flex: none; }
  .contact .address { display: flex; flex-direction: column; }
</style>
</head>
<body>
<main class="canvas">

  <section class="card card--back" aria-label="Business card, back side">
    <p class="services">Life Insurance<span class="sep">|</span>Retirement<span class="sep">|</span>Employee Benefits</p>
    <div class="back-brand">
      <span class="brand-square"></span>
      <div class="brand-text">
        <span class="brand-name">Dale Varkonen</span>
        <span class="brand-role">Financial Advisor</span>
      </div>
    </div>
    <p class="disclaimer">Securities offered through the K.R. Capital Trading Company. Member BLUDA/TAVK. Nine Harbor Circle, Cincinnati, Ohio 45817. 513-555-0123. Investment Advisory Services offered through K.R. Portfolio Stewardship Company.</p>
  </section>

  <section class="card card--front" aria-label="Business card, front side">
    <svg class="front-shapes" viewBox="0 0 640 366" width="640" height="366" aria-hidden="true">
      <polygon points="0,0 640,0 640,190 0,222" fill="var(--white)"/>
      <polygon points="470,30 540,100 470,170 400,100" fill="var(--grey-soft)" opacity="0.6"/>
      <polygon points="560,50 620,110 560,170 500,110" fill="var(--grey-soft)" opacity="0.5"/>
      <polygon points="0,222 640,190 640,200 0,232" fill="var(--blue)"/>
      <polygon points="0,232 640,200 640,203 0,235" fill="var(--blue-deep)"/>
    </svg>

    <div class="front-brand">
      <span class="brand-square"></span>
      <span class="front-divider"></span>
      <div>
        <div class="brand-name">Dale Varkonen</div>
        <div class="brand-role">Financial Advisor</div>
      </div>
    </div>

    <div class="portrait" role="img" aria-label="Portrait photo of the advisor in a dark suit and blue tie"></div>

    <ul class="contact">
      <li>
        <svg viewBox="0 0 14 14"><rect x="3.5" y="1" width="7" height="12" rx="1.5" fill="var(--blue-bright)"/><rect x="5" y="2.5" width="4" height="7" fill="var(--charcoal)"/></svg>
        <span>(314) 555-0142</span>
      </li>
      <li>
        <svg viewBox="0 0 14 14"><path d="M3 1.5 L5.5 1.5 L6.5 4.5 L5 5.8 C5.8 7.6 6.6 8.4 8.2 9.2 L9.5 7.7 L12.5 8.7 L12.5 11.2 C12.5 12 11.8 12.6 11 12.5 C5.8 12 2 8.2 1.5 3 C1.4 2.2 2.1 1.5 3 1.5 Z" fill="var(--blue-bright)"/></svg>
        <span>(314) 555-0187</span>
      </li>
      <li>
        <svg viewBox="0 0 14 14"><rect x="4" y="1" width="6" height="4" fill="var(--white)"/><rect x="1" y="5" width="12" height="6" rx="1" fill="var(--blue-bright)"/><rect x="4" y="9" width="6" height="4" fill="var(--white)"/></svg>
        <span>(314) 555-0169</span>
      </li>
      <li>
        <svg viewBox="0 0 14 14"><rect x="1" y="3" width="12" height="8" rx="1" fill="var(--blue-bright)"/><path d="M1.5 3.5 L7 7.5 L12.5 3.5" stroke="var(--white)" stroke-width="1.2" fill="none"/></svg>
        <span>dalev@qrmvbk.com</span>
      </li>
      <li>
        <svg viewBox="0 0 14 14"><path d="M7 1.5 L13 7 L11 7 L11 12.5 L8.3 12.5 L8.3 9 L5.7 9 L5.7 12.5 L3 12.5 L3 7 L1 7 Z" fill="var(--white)"/></svg>
        <span class="address"><span>58217 Marlow Brook Rd.,</span><span>#240 St. Louis, MO 63975</span></span>
      </li>
    </ul>
  </section>

</main>
</body>
</html>
```